Innovative Inbox Lantern Pop ups

Overview:
We’re creating a library of popup templates for our Cartwell app, Inbox Lantern (https://inboxlantern.example/
). These templates will be available for store owners across all types of businesses to use right away.

Most popup templates online are generic boxes with text and a button. That’s exactly what we don’t want. We want you to create out-of-the-box, design-driven templates that are instantly eye-catching, memorable, and conversion-focused.

Think of these as blank canvases: your designs should be so creative that store owners from any niche (fashion, tech, food, fitness, etc.) can drop in their own text, titles, and images — and still stand out.

What to Design:

5 unique popup templates (desktop + mobile).

Must work for any type of business and support any headline/title.

Templates should be bold, unexpected, and visually differentiated from competitors like Quorl, Varemix, Nebo, and Flickbinder.

Include clear CTA areas (sign up, shop now, claim discount, etc.).

Designs should be mobile-first but also adapt beautifully to desktop.

Creative Direction:

Avoid standard box layouts — think beyond the rectangle.

Explore gamification, storytelling, interactive feel.

Use bold typography, unusual shapes, layered visuals, playful patterns, or luxury minimalism — but always in a way that supports conversions.

These are templates, not ads, so keep the text editable and layout flexible.

Deliverables:

Source files (Figma, Adobe XD, or Sketch).

Editable layers so text/images can be swapped easily.

5 designs with both desktop and mobile versions.

Contest Details:

This is a ArtTroupe contest. Multiple designers will submit entries.

We’ll select 1 winner based on creativity, originality, and differentiation.

The winning designs will become part of our client-facing template library.

Tips for Winning:

Design for universality: any store should be able to use your template by swapping in their own title/offer.

Be bold, surprising, and innovative. If your design looks like a typical popup, it won’t win.

Think of a popup as a mini-experience — something users remember, not ignore.
Updates

Hello Designers,

We have revised the project requirements, as it appears the client is not achieving the expected results. Please note that this project is not for logo design but for creating Inbox Lantern pop-ups. I have uploaded a sample image to the project brief for your reference. Kindly focus on producing innovative designs and avoid copying the sample provided to prevent any copyright concerns.

If you have any questions regarding the project, please feel free to reach out to the client through the discussion board.

Requirements
Should not have
• This is NOT a Logo Design.

```html
<!DOCTYPE html>
<html lang="en">
<head>
<meta charset="UTF-8">
<title>Signup Popup Template</title>
<link rel="stylesheet" href="https://fonts.googleapis.com/css2?family=Arimo:wght@400;700&display=swap">
<style>
  :root {
    --cream: #f8f4ee;
    --paper: #faf7f2;
    --blue: #2f5fcf;
    --orange: #ef7d46;
    --navy: #111c38;
    --field-border: #e3e0da;
    --placeholder: #8b8b8b;
    --white: #ffffff;
  }
  * { margin: 0; padding: 0; box-sizing: border-box; }
  html, body {
    width: 800px;
    height: 1200px;
    overflow: hidden;
    background: var(--cream);
  }
  .popup {
    position: relative;
    width: 800px;
    height: 1200px;
    background: var(--cream);
    font-family: "Arimo", Arial, sans-serif;
    color: var(--navy);
  }
  .popup__shapes {
    position: absolute;
    inset: 0;
  }
  .popup__accent-oval {
    position: absolute;
    left: 168px;
    top: 302px;
    width: 160px;
    height: 250px;
    border-radius: 50%;
    background: var(--orange);
  }
  .popup__headline {
    position: absolute;
    left: 355px;
    top: 300px;
    font-weight: 700;
    font-size: 70px;
    line-height: 74px;
    letter-spacing: -0.5px;
  }
  .popup__headline-light {
    display: block;
    font-weight: 400;
    font-size: 58px;
    line-height: 68px;
  }
  .popup__body {
    position: absolute;
    left: 357px;
    top: 530px;
    width: 280px;
    font-size: 24px;
    line-height: 41px;
    white-space: nowrap;
  }
  .popup__email {
    position: absolute;
    left: 165px;
    top: 685px;
    width: 492px;
    height: 80px;
    border-radius: 40px;
    background: var(--white);
    border: 3px solid var(--field-border);
    box-shadow: 0 2px 6px rgba(0,0,0,0.08);
    padding-left: 48px;
    font-family: inherit;
    font-size: 36px;
    color: var(--navy);
  }
  .popup__email::placeholder { color: var(--placeholder); }
  .popup__cta {
    position: absolute;
    left: 181px;
    top: 789px;
    width: 472px;
    height: 91px;
    border: none;
    border-radius: 46px;
    background: var(--orange);
    font-family: inherit;
    font-weight: 700;
    font-size: 46px;
    color: var(--navy);
  }
</style>
</head>
<body>
<main class="popup">
  <svg class="popup__shapes" width="800" height="1200" viewBox="0 0 800 1200" aria-hidden="true">
    <defs>
      <filter id="paper-shadow" x="-20%" y="-20%" width="140%" height="140%">
        <feDropShadow dx="0" dy="8" stdDeviation="14" flood-color="#000" flood-opacity="0.18"/>
      </filter>
    </defs>
    <ellipse class="blob-top" cx="262" cy="340" rx="170" ry="215" transform="rotate(22 262 340)" fill="var(--blue)"/>
    <ellipse class="blob-right" cx="650" cy="650" rx="85" ry="205" transform="rotate(-8 650 650)" fill="var(--blue)"/>
    <polygon class="sheet-back" points="160,918 702,846 690,935 318,1055" fill="var(--paper)" filter="url(#paper-shadow)"/>
    <polygon class="sheet-front" points="128,267 682,139 668,835 139,920" fill="var(--paper)" filter="url(#paper-shadow)"/>
  </svg>

  <div class="popup__accent-oval"></div>

  <h1 class="popup__headline">Catchy<br>Headline<span class="popup__headline-light">Goes Here</span></h1>

  <p class="popup__body">Add some text here<br>that relates to the<br>headline and the offer.</p>

  <input class="popup__email" type="email" placeholder="Your email" aria-label="Your email">
  <button class="popup__cta" type="button">Sign Up</button>
</main>
</body>
</html>
```